Hockey Sponsorship Proposal

We are looking for a sponsorship proposal design for an apparel company to supply our hockey camps with jerseys and apparel. We want to use lots of visuals so potential business partners can see the exposure and publicity their company could get by working with us. We would like the primary colors to be red, black and white. We have attached a bunch of images but not all need to be used. We would like to see a mix of images with adult players and youth players where appropriate. Although I have provided a rough outline for the information on the powerpoint the text and images can be displayed however you would like.

Here is a link to some proposals to give you an idea of what we are looking for
https://www.quillrack.co.uk/pin/512604837219056471/

Target Market(s)

Athletic Apparel Companies

Industry/Entity Type

It Company

Requirements
Must have
• Please note this should be suitable for web as the proposal will be emailed. This is NOT for print.
Nice to have
• I would like the first page to have a full image as the backdrop with the text over top if possible.

```html
<!DOCTYPE html>
<html lang="en">
<head>
<meta charset="utf-8">
<title>Garrett Holloway Hockey – Request for Proposal</title>
<link href="https://fonts.googleapis.com/css2?family=Alfa+Slab+One&family=Montserrat:wght@400;500;700;900&display=swap" rel="stylesheet">
<style>
  :root{
    --red:#d7141a;
    --black:#141414;
    --ink:#1d1d1d;
    --paper:#ececec;
    --white:#ffffff;
    --bg:#e1e5e3;
    --muted:#9a9a9a;
    --grey-photo-a:#8a8a8a;
    --grey-photo-b:#3a3a3a;
  }
  *{box-sizing:border-box;margin:0;padding:0}
  html,body{width:1200px;height:1200px;overflow:hidden;background:var(--bg);font-family:"Montserrat",sans-serif}
  .canvas{position:relative;width:1200px;height:1200px}
  .spread{position:absolute;left:50px;width:1100px;height:440px;display:flex;box-shadow:0 14px 30px rgba(0,0,0,.18)}
  .spread--cover{top:100px}
  .spread--inside{top:660px}
  .page{position:relative;width:550px;height:440px;overflow:hidden}
  .page--dark{background:linear-gradient(135deg,#262626 0%,var(--black) 60%,#0b0b0b 100%);color:var(--white)}
  .page--light{background:var(--paper);color:var(--ink)}

  /* brand line */
  .brand{display:flex;align-items:center;gap:10px}
  .brand__mark{width:14px;height:14px;background:var(--red);flex:none}
  .brand__name{font-family:"Montserrat",sans-serif;font-weight:900;letter-spacing:.04em;text-transform:uppercase}
  .brand__tag{font-size:9px;letter-spacing:.06em;font-weight:400}

  /* back cover */
  .back-cover__brand{position:absolute;left:60px;bottom:110px}
  .back-cover__brand .brand__name{font-size:20px;color:var(--white)}
  .back-cover__tag{position:absolute;left:84px;bottom:92px;color:var(--muted)}
  .back-cover__contact{position:absolute;left:60px;bottom:40px;width:440px;font-size:10px;line-height:1.7;color:var(--muted)}
  .back-cover__contact strong{color:var(--white);font-weight:700}

  /* front cover */
  .cover__photo{position:absolute;left:60px;top:70px;width:420px;height:190px;background:linear-gradient(180deg,#b9b9b9 0%,var(--grey-photo-a) 40%,var(--grey-photo-b) 100%)}
  .cover__brand{position:absolute;left:40px;top:30px}
  .cover__brand .brand__name{font-size:14px;color:var(--red)}
  .cover__tag{position:absolute;left:64px;top:50px;color:#555}
  .cover__blocks{position:absolute;right:0;top:0}
  .cover__title{position:absolute;left:80px;top:262px;font-family:"Alfa Slab One",serif;font-size:36px;line-height:1.05;text-transform:uppercase;color:var(--black);z-index:1}
  .cover__title span{display:block;color:var(--red)}
  .cover__year{position:absolute;left:82px;top:354px;font-size:11px;color:#777;letter-spacing:.08em}

  /* inside left */
  .about__photo{position:absolute;left:190px;top:46px;width:360px;height:300px;background:linear-gradient(160deg,#9c9c9c 0%,#6e6e6e 50%,#d2d2d2 100%)}
  .about__title{position:absolute;left:60px;top:160px;font-family:"Alfa Slab One",serif;text-transform:uppercase;line-height:1.05}
  .about__line{display:block;font-size:38px;color:var(--black)}
  .about__line--band{margin-top:6px;display:inline-block;background:var(--red);color:var(--white);padding:2px 12px 4px;margin-left:-12px;font-size:38px}

  /* inside right */
  .opp__photo{position:absolute;left:60px;top:46px;width:90px;height:300px;background:linear-gradient(160deg,#a4a4a4,#6a6a6a)}
  .opp__list{position:absolute;left:160px;top:140px;width:280px;list-style:none;font-size:11px;line-height:1.45;color:#e6e6e6;z-index:2}
  .opp__list li{position:relative;padding-left:14px;margin-bottom:12px}
  .opp__list li::before{content:"";position:absolute;left:0;top:4px;width:6px;height:6px;background:var(--red)}
  .opp__people{position:absolute;right:30px;bottom:0;width:190px;height:140px;background:linear-gradient(90deg,#1b1b1b 0%,#2a2a2a 50%,#a8141a 75%,#1f3a8a 100%);opacity:.9}
  .stripes{position:absolute}
  .stripes--top{right:0;top:0}
  .stripes--bottom{left:300px;bottom:0}
</style>
</head>
<body>
<main class="canvas">

  <section class="spread spread--cover">
    <article class="page page--dark back-cover">
      <div class="brand back-cover__brand"><span class="brand__mark"></span><span class="brand__name">Garrett Holloway Hockey</span></div>
      <p class="brand__tag back-cover__tag">Uniform and Apparel Partnership Opportunity</p>
      <p class="back-cover__contact">If you are interested in partnering with Garrett on this opportunity please contact Miles Draper at<br><strong>555.014.2290</strong> or via email <strong>miles.draper@hollowayhockey.com</strong></p>
    </article>

    <article class="page page--light cover">
      <div class="cover__photo" role="img" aria-label="Black and white team photo of hockey camp players gathered on the ice"></div>
      <div class="brand cover__brand"><span class="brand__mark"></span><span class="brand__name">Garrett Holloway Hockey</span></div>
      <p class="brand__tag cover__tag">Uniform and Apparel Partnership Opportunity</p>
      <svg class="cover__blocks" width="170" height="440" viewBox="0 0 170 440" aria-hidden="true">
        <rect x="40" y="20" width="40" height="50" fill="#d7141a"/>
        <rect x="80" y="0" width="30" height="60" fill="#141414"/>
        <rect x="90" y="110" width="50" height="170" fill="#d7141a"/>
        <rect x="65" y="150" width="30" height="130" fill="#141414"/>
        <rect x="140" y="160" width="30" height="80" fill="#141414"/>
        <rect x="20" y="220" width="50" height="70" fill="#d7141a"/>
        <rect x="95" y="260" width="20" height="30" fill="#d7141a"/>
      </svg>
      <h1 class="cover__title">Request for<span>Proposal</span></h1>
      <p class="cover__year">2017 - 2018</p>
    </article>
  </section>

  <section class="spread spread--inside">
    <article class="page page--light about">
      <div class="about__photo" role="img" aria-label="Black and white photo of hockey players skating during a camp scrimmage"></div>
      <h2 class="about__title"><span class="about__line">About</span><span class="about__line">This</span><span class="about__line--band">Opportunity</span></h2>
    </article>

    <article class="page page--dark opportunity">
      <div class="opp__photo" role="img" aria-label="Continuation of the black and white scrimmage photo"></div>
      <svg class="stripes stripes--top" width="150" height="130" viewBox="0 0 150 130" aria-hidden="true">
        <polygon points="20,0 40,0 10,40 -10,40" fill="#ffffff"/>
        <polygon points="60,0 90,0 30,120 0,120" fill="#d7141a"/>
        <polygon points="95,0 110,0 90,40 75,40" fill="#ffffff"/>
        <polygon points="120,0 150,0 110,70 80,70" fill="#d7141a"/>
      </svg>
      <ul class="opp__list">
        <li>Garrett Holloway is seeking a partner to be his official jersey and apparel supplier.</li>
        <li>Selected supplier will outfit all participants of Garrett’s PHL and youth hockey camps.</li>
        <li>Opportunity to outfit 50 PHL superstars and over 400 of North America’s top young hockey players.</li>
      </ul>
      <div class="opp__people" role="img" aria-label="Coach in a black jacket talking with a player in a red and blue practice jersey"></div>
      <svg class="stripes stripes--bottom" width="110" height="100" viewBox="0 0 110 100" aria-hidden="true">
        <polygon points="40,0 60,0 10,100 -10,100" fill="#ffffff"/>
        <polygon points="65,20 90,20 50,100 25,100" fill="#d7141a"/>
        <polygon points="90,60 110,60 90,100 70,100" fill="#ffffff"/>
      </svg>
    </article>
  </section>

</main>
</body>
</html>
```